Brochure Design Project

Looking for brochure design for a sell sheet that our sales team will use in the field. We offer buyers and mills of board and dimension lumber with an avenue to transact lumber sales directly, without using a middleman. The buyer posts their needs, and the mills use competitive quoting to offer their pricing. This is not a reverse auction, as our motto is "The Best Product at the Best Price Without the Battle". The buyer does not have to take the lowest price, so it is not an auction. We would like a 8x11, bi fold (4 sides) landscape format. We would like to choose the design first, and then provide the text and photos once the designer is chosen. Please use backgrounds and colors that have a feel of the outdoors, wood grain, forest, saw mill, lumber. Please visit out site at www.plankverde.com to get a feel for our product.

Pages- (These are just generalizations of what will go on each page)
Page 1: Logo, Area for slogan, Photo
Page 2: Photos, who we are, what we do, what we sell
Page 3 : Photos, Description area for our "Clear Rate Scout" and "Clear Rate Ledger" features
Page 4: A list of Plankverde's commitments to our business partners, photos

Target Market(s)

This is for the buyer of lumber at retail lumber yards, and window, door, pallet, log home, modular home, and other manufacturers.

Industry/Entity Type

Landscape

Requirements
Must have
• 4 pages , landscape format

```html
<!DOCTYPE html>
<html lang="en">
<head>
<meta charset="utf-8">
<title>Plankverde Sell Sheet – Bi-fold Layout</title>
<link rel="stylesheet" href="https://fonts.googleapis.com/css2?family=PT+Serif:wght@400;700&family=Arimo:ital,wght@0,400;0,700;1,700&display=swap">
<style>
:root{
  --canvas:#000;
  --label:#4a4a4a;
  --forest-light:#86a95a;
  --panel-dark:#22241e;
  --panel-deep:#161712;
  --wood-light:#a87a4c;
  --wood-mid:#7a5331;
  --wood-glow:#d99a2a;
  --brand-green:#3f8f3a;
  --table-head:#7d9c32;
  --table-row:#f4dd97;
  --table-line:#c99c3c;
  --table-text:#2b2410;
  --ink:#111;
  --white:#fff;
}
*{box-sizing:border-box;margin:0;padding:0}
html,body{width:1200px;height:1017px;overflow:hidden;background:var(--canvas)}
body{position:relative;font-family:"Arimo",Arial,sans-serif}
.page{position:absolute;overflow:hidden}
.photo{position:absolute}
.label{position:absolute;font-family:"PT Serif",Georgia,serif;color:var(--label);font-size:40px;letter-spacing:.5px}

.wood-frame{position:absolute;background:linear-gradient(90deg,var(--wood-mid),var(--wood-light) 45%,var(--wood-mid));border-radius:10px;box-shadow:0 3px 8px rgba(0,0,0,.6)}
.mark{position:absolute;width:30px;height:30px;border-radius:50%;border:2px solid var(--brand-green);background:rgba(255,255,255,.08)}

/* About page */
.about{left:20px;top:59px;width:630px;height:429px}
.about .bg{inset:0;background:linear-gradient(180deg,#5e8a3c 0%,#3c6a2a 30%,#1f3d1a 70%,#2a2418 100%)}
.about h1{position:absolute;left:29px;top:6px;font-family:"PT Serif",Georgia,serif;font-weight:400;font-size:27px;color:var(--ink)}
.about .intro{position:absolute;left:29px;top:38px;width:350px;font-family:"PT Serif",Georgia,serif;font-size:10px;line-height:12px;color:var(--ink)}
.about .left-frame{left:20px;top:79px;width:140px;height:326px}
.about .left-inner{position:absolute;left:12px;top:42px;width:124px;height:272px;background:var(--panel-dark)}
.about .right-frame{left:462px;top:3px;width:143px;height:354px;border-radius:8px 8px 28px 28px}
.about .right-inner{position:absolute;left:10px;top:25px;width:124px;height:274px;background:var(--panel-dark)}
.callout{position:absolute;height:40px;font-size:9px;line-height:11px;padding:5px 10px 0 30px;border-radius:20px 0 0 20px}
.callout.light{left:181px;width:292px;background:linear-gradient(180deg,#fff,#d9d9d2);color:var(--ink)}
.callout.dark{left:160px;width:307px;background:var(--panel-deep);color:#e7e7e0;border:1px solid #6c6c60;padding-left:12px;border-radius:0 20px 20px 0}
.about .closing{position:absolute;left:217px;top:372px;width:360px;font-size:10px;line-height:12px;color:var(--white)}

/* Front cover */
.front{left:666px;top:59px;width:504px;height:348px}
.front .bg{inset:0;background:radial-gradient(ellipse 200px 130px at 390px 170px,var(--wood-glow),transparent 80%),linear-gradient(90deg,#6f4a2b,#8c6139 40%,#5d3d22 100%)}
.front .card{position:absolute;background:linear-gradient(90deg,var(--wood-mid),var(--wood-light));border-radius:8px 8px 26px 8px;box-shadow:0 4px 10px rgba(0,0,0,.7)}
.front .card-top{left:-6px;top:44px;width:175px;height:140px;transform:rotate(-8deg)}
.front .card-bottom{left:-4px;top:176px;width:250px;height:150px}
.brand{font-family:"Arimo",Arial,sans-serif;font-weight:700;color:var(--brand-green);position:absolute;white-space:nowrap}
.front .brand{left:278px;top:166px;font-size:31px}
.front .slogan{position:absolute;left:278px;top:206px;font-size:11px;font-weight:700;font-style:italic;color:#1c1208;white-space:nowrap}

/* Rates page */
.rates{left:20px;top:492px;width:630px;height:432px;background:var(--panel-dark)}
.rates .band{position:absolute;left:0;top:0;width:630px;height:62px;background:linear-gradient(90deg,#1a1b16 0%,#23261d 70%,var(--forest-light) 84%,#8fb04c 100%)}
.rates h2{position:absolute;left:27px;font-family:"PT Serif",Georgia,serif;font-weight:400;font-size:19px;color:var(--white)}
.rate-table{position:absolute;left:27px;width:484px;border-collapse:collapse;border:2px solid #fff;font-size:10px;color:var(--table-text);box-shadow:0 2px 6px rgba(0,0,0,.6)}
.rate-table th{background:var(--table-head);color:#f6f2d8;font-weight:700;height:27px;font-size:10px;line-height:11px;border-right:1px solid #c9b86d}
.rate-table td{background:var(--table-row);height:27px;border-right:1px solid var(--table-line);border-top:1px solid #fff3c8;padding-left:6px;font-weight:700;font-size:9px}
.rate-table td.mill{text-align:center;font-size:12px;padding-left:0}
.rate-table td small{font-weight:400}
.rates .note{position:absolute;left:27px;width:420px;font-size:10px;line-height:12px;color:var(--white)}
.rates .side-frame{left:519px;top:5px;width:93px;height:402px;border-radius:0 30px 30px 0}

/* Back cover */
.back{left:666px;top:492px;width:504px;height:346px}
.back .bg{inset:0;background:linear-gradient(90deg,#8a6a47,#a98157 50%,#6e4a2b 85%,#4a2a15 100%)}
.back .halo{position:absolute;left:345px;top:-10px;width:200px;height:260px;border-radius:50%;background:rgba(40,22,10,.35)}
.back .strip{position:absolute;left:0;top:53px;width:340px;height:173px;background:var(--panel-deep)}
.back .text-panel{position:absolute;left:98px;top:63px;width:124px;height:152px;overflow:hidden;background:linear-gradient(135deg,#f5eed8,#e6d6a8);padding:12px 8px;font-size:6.8px;line-height:8.4px;color:#222;text-align:justify}
.back .text-panel p+p{margin-top:7px}
.back .tab{left:340px;top:59px;width:62px;height:170px;border-radius:0 14px 14px 0}
.back .brand{left:281px;top:276px;width:170px;text-align:center;font-size:21px;color:#6fa447}
.back .footer{position:absolute;left:226px;top:305px;width:270px;text-align:center;font-size:7px;line-height:9px;color:#e9e0cc}
</style>
</head>
<body>

<section class="page about">
  <div class="photo bg" role="img" aria-label="Sunlit forest with stacked lumber in the background"></div>
  <h1>About plankverde</h1>
  <p class="intro">fyl a iugag asgas aiigasg saghoaho asioyiz idag iagig agailg asguas giags agsigsaig aatdfwu asasu fsaasfsfasjfasjfsaj fasj fasfs f</p>

  <div class="wood-frame left-frame">
    <span class="mark" style="left:55px;top:6px"></span>
    <div class="left-inner">
      <div class="photo" role="img" aria-label="Stacked cut boards, end grain" style="left:3px;top:7px;width:118px;height:80px;background:linear-gradient(135deg,#c9693f,#e9b98a 50%,#a35a34)"></div>
      <div class="photo" role="img" aria-label="Close view of dimension lumber" style="left:3px;top:93px;width:118px;height:85px;background:linear-gradient(135deg,#8a6a45,#c7a272 50%,#6b4f33)"></div>
      <div class="photo" role="img" aria-label="Stack of fresh planks" style="left:3px;top:184px;width:118px;height:80px;background:linear-gradient(135deg,#d8b480,#f0d7a8 50%,#a9824f)"></div>
    </div>
  </div>

  <div class="wood-frame right-frame">
    <span class="mark" style="left:56px;top:309px"></span>
    <div class="right-inner">
      <div class="photo" role="img" aria-label="Bundled red timber ends" style="left:3px;top:9px;width:118px;height:78px;background:linear-gradient(135deg,#b4553a,#e0b08a 55%,#8c3f2a)"></div>
      <div class="photo" role="img" aria-label="Sawn beams in a yard" style="left:3px;top:97px;width:118px;height:82px;background:linear-gradient(135deg,#7d6448,#b5936a 50%,#5b4530)"></div>
      <div class="photo" role="img" aria-label="Stacked lumber lengths" style="left:3px;top:188px;width:118px;height:80px;background:linear-gradient(135deg,#b58b5a,#e3c497 50%,#8a6a44)"></div>
    </div>
  </div>

  <p class="callout light" style="top:77px">Lorem ipsum dolor sit amet, consectetur adipiscing elit. Integer Nunc sollicitudin, arcu ornare. Pellentesque iaculis risus sed ante commodo, a l fringilla.</p>
  <p class="callout dark" style="top:124px">Lorem ipsum dolor sit amet, consectetur adipiscing elit. Integer Nunc sollicitudin, arcu ornare. Pellentesque iaculis risus sed ante commodo, a l fringilla.</p>
  <p class="callout light" style="top:173px">Lorem ipsum dolor sit amet, consectetur adipiscing elit. Integer Nunc sollicitudin, arcu ornare. Pellentesque iaculis risus sed ante commodo, a l fringilla.</p>
  <p class="callout dark" style="top:218px">Lorem ipsum dolor sit amet, consectetur adipiscing elit. Integer Nunc sollicitudin, arcu ornare. Pellentesque iaculis risus sed ante commodo, a l fringilla.</p>
  <p class="callout light" style="top:266px">Lorem ipsum dolor sit amet, consectetur adipiscing elit. Integer Nunc sollicitudin, arcu ornare. Pellentesque iaculis risus sed ante commodo, a l fringilla.</p>
  <p class="callout dark" style="top:311px">Lorem ipsum dolor sit amet, consectetur adipiscing elit. Integer Nunc sollicitudin, arcu ornare. Pellentesque iaculis risus sed ante commodo, a l fringilla.</p>

  <p class="closing">fyl a iugag asgas aiigasg saghoaho asioyiz idag iagig agailg asguas giags agsigsaig aatdfwu asasu fsaasfsfasjfasjfsaj fasj fasfs ffssuysuy tyafyfsgisugisgilsguiisugisgiusgilssugilugslugsosgolss</p>
</section>

<section class="page front">
  <div class="photo bg" role="img" aria-label="Warm wood grain background with golden light"></div>
  <div class="card card-top">
    <div class="photo" role="img" aria-label="Pile of cut logs beside a forest" style="left:6px;top:6px;width:140px;height:124px;background:linear-gradient(160deg,#6d7a66,#c9a77a 45%,#8a6a48)"></div>
    <span class="mark" style="left:150px;top:30px;width:20px;height:20px"></span>
  </div>
  <div class="card card-bottom">
    <div class="photo" role="img" aria-label="Stacked lumber in a sawmill yard" style="left:6px;top:10px;width:185px;height:132px;background:linear-gradient(160deg,#a9b6c0,#e0c79b 40%,#a5804f)"></div>
    <span class="mark" style="left:210px;top:55px;width:20px;height:20px"></span>
  </div>
  <span class="mark" style="left:282px;top:122px;width:36px;height:36px"></span>
  <span class="brand">plankverde</span>
  <p class="slogan">Position slogan here,position slogan!</p>
</section>
<div class="label" style="right:30px;top:415px">Front Cover</div>

<section class="page rates">
  <div class="band"></div>
  <div class="photo" role="img" aria-label="Wood chips" style="left:519px;top:150px;width:111px;height:282px;background:linear-gradient(160deg,#6a4a2c,#3a2615 60%,#7d5a38)"></div>
  <div class="photo" role="img" aria-label="Wood chips" style="left:0;top:405px;width:630px;height:27px;background:linear-gradient(90deg,#3a2615,#6a4a2c 50%,#3a2615)"></div>
  <div class="wood-frame side-frame">
    <span class="mark" style="left:6px;top:198px;width:36px;height:36px"></span>
  </div>

  <h2 style="top:8px">Clear Rate Scout</h2>
  <table class="rate-table" style="top:35px">
    <colgroup><col style="width:148px"><col style="width:101px"><col style="width:160px"><col style="width:75px"></colgroup>
    <tr><th>Mill/Supplier</th><th>Per 1000 MBF Price</th><th>Freight on Board with Shipping</th><th>Landed Cost</th></tr>
    <tr><td class="mill">Mill A</td><td>$ 459.00 <small>USD</small></td><td>$ 51,408.00 <small>USD</small> [1]</td><td>$ 53,464.32 <small>USD</small></td></tr>
    <tr><td class="mill">Mill B</td><td>$ 460.00 <small>USD</small></td><td>$ 51,520.00 <small>USD</small> [2]</td><td>$ 53,580.80 <small>USD</small></td></tr>
    <tr><td class="mill">Mill C</td><td>$ 420.00 <small>USD</small></td><td>$ 52,752.00 <small>USD</small> [3]</td><td>$ 54,862.08 <small>USD</small></td></tr>
  </table>
  <p class="note" style="top:160px;width:380px">Lorem ipsum dolor sit amet, consectetur adipiscing elit. Integer Nunc sollicitudin, arcu ornare. Pellentesque iaculis risus sed ante commodo, a dignissim nisl fringilla.</p>
  <div class="photo" role="img" aria-label="Lumber buyer in a hard hat on the phone" style="left:407px;top:150px;width:112px;height:74px;background:linear-gradient(135deg,#c98f6a,#a8584a 55%,#5a3a2c)"></div>

  <h2 style="top:224px">Clear Rate Ledger</h2>
  <table class="rate-table" style="top:251px">
    <colgroup><col style="width:148px"><col style="width:101px"><col style="width:160px"><col style="width:75px"></colgroup>
    <tr><th>Mill/Supplier</th><th>Per 1000 MBF Price</th><th>Freight on Board with Shipping</th><th>Landed Cost</th></tr>
    <tr><td class="mill">Mill A</td><td>$ 459.00 <small>USD</small></td><td>$ 51,408.00 <small>USD</small> [1]</td><td>$ 53,464.32 <small>USD</small></td></tr>
    <tr><td class="mill">Mill B</td><td>$ 460.00 <small>USD</small></td><td>$ 51,520.00 <small>USD</small> [2]</td><td>$ 53,580.80 <small>USD</small></td></tr>
    <tr><td class="mill">Mill C</td><td>$ 420.00 <small>USD</small></td><td>$ 52,752.00 <small>USD</small> [3]</td><td>$ 54,862.08 <small>USD</small></td></tr>
  </table>
  <p class="note" style="top:370px">Lorem ipsum dolor sit amet, consectetur adipiscing elit. Integer Nunc sollicitudin, arcu ornare. Pellentesque iaculis risus sed ante commodo, a dignissim nisl fringilla.</p>
</section>
<div class="label" style="left:405px;top:938px">Inner Spread</div>

<section class="page back">
  <div class="photo bg" role="img" aria-label="Wood grain background"></div>
  <div class="halo"></div>
  <div class="strip">
    <div class="photo" role="img" aria-label="Pale pine boards" style="left:2px;top:8px;width:90px;height:157px;background:linear-gradient(90deg,#e8d6b0,#c9a877 50%,#f0e2c2)"></div>
    <div class="photo" role="img" aria-label="Stacked red lumber ends" style="left:228px;top:8px;width:106px;height:157px;background:linear-gradient(135deg,#b4553a,#e2a772 50%,#7e3a24)"></div>
  </div>
  <div class="text-panel">
    <p>Lorem ipsum dolor sit amet, consectetur adipiscing elit. Integer Nunc sollicitudin, arcu ornare. Pellentesque iaculis risus sed ante commodo, a dignissim nisl fringilla.</p>
    <p>Mauris tempor mauris vitae neque ornare dui at sem porttitor placerat. Quisque eget dapibus libero. Duis egestas faucibus libero, at accumsan ante dignissim sit amet.</p>
  </div>
  <div class="wood-frame tab">
    <span class="mark" style="left:18px;top:70px;width:24px;height:24px"></span>
  </div>
  <div class="photo" role="img" aria-label="Sawmill worker cutting a log" style="left:0;top:232px;width:203px;height:114px;background:linear-gradient(135deg,#5a6b78,#a08a6a 50%,#4a3a2a)"></div>
  <span class="mark" style="left:354px;top:246px;width:24px;height:24px"></span>
  <span class="brand">plankverde</span>
  <p class="footer">Lorem ipsum dolor sit amet, consectetur adipiscing elit. Integer Nunc sollicitudin, arcu ornare. Pellentesque iaculis risus sed ante commodo.</p>
</section>
<div class="label" style="right:33px;top:846px">Back Cover</div>

</body>
</html>
```